Tidal Spoon is a modern and professional services business in the field of hospitality.

Need business card for a professional chef and consultant. Attention to detail and to stand out is our goal. I want a professional and stand out card which is not generic.
Would like a modern card with black gold or blue I’m not very sure on colours yet , open to ideas from those in the know. This is my second project and have been really happy with the process so far.
With 15 years in the hospitality industry I am launching into consulting and starting my own business. I’d like a few types of designs to look at which style I want. Open to suggestions. Thanks in advance for the work. I want something that will become part of my brand as it is launched. There is a chance for possible future work to the right person.

Target Market(s)

Restauranters and Registered training organisations.

Industry/Entity Type

Professional Service

Font styles to use
Serif

Colors

Designer to choose colors to be used in the design.

Requirements
Must have
• A stand out design, blue / black
Nice to have
• Can u get embossed cards?
Should not have
• Na

```html
<!DOCTYPE html>
<html lang="en">
<head>
<meta charset="utf-8">
<title>Tidal Spoon — Business Card</title>
<link rel="stylesheet" href="https://fonts.googleapis.com/css2?family=Playfair+Display:wght@600&family=Lora:wght@400;700&display=swap">
<style>
  :root {
    --backdrop: #3b3532;
    --card: #0d0d0d;
    --card-edge: #1c1c1c;
    --brand-grey: #a3a3a3;
    --silver: #c9c9c9;
    --accent-blue: #3f95e0;
    --text-light: #e6e6e6;
    --divider: #2e2e2e;
  }
  * { margin: 0; padding: 0; box-sizing: border-box; }
  html, body {
    width: 1200px;
    height: 900px;
    overflow: hidden;
    background: var(--backdrop);
  }
  .stage {
    position: relative;
    width: 1200px;
    height: 900px;
    display: flex;
    align-items: center;
    justify-content: center;
    gap: 60px;
  }
  .card {
    position: relative;
    width: 525px;
    height: 300px;
    background: var(--card);
    border: 1px solid var(--card-edge);
    box-shadow: 0 14px 30px rgba(0, 0, 0, 0.45);
    overflow: hidden;
  }

  /* Front: brand + contact */
  .card-front { display: flex; }
  .brand-panel {
    width: 52%;
    display: flex;
    align-items: flex-end;
    justify-content: center;
    padding: 0 12px 48px;
  }
  .brand-name {
    font-family: "Playfair Display", serif;
    font-weight: 600;
    font-size: 32px;
    letter-spacing: 1px;
    color: var(--brand-grey);
    text-transform: uppercase;
    line-height: 1;
    white-space: nowrap;
  }
  .contact-panel {
    width: 48%;
    border-left: 1px solid var(--divider);
    margin: 40px 0;
    padding: 6px 0 0 24px;
    font-family: "Lora", serif;
    color: var(--text-light);
  }
  .person-name {
    font-weight: 700;
    font-size: 16px;
    letter-spacing: 0.5px;
    color: var(--accent-blue);
    text-transform: uppercase;
    line-height: 1.15;
  }
  .person-role {
    font-size: 12.5px;
    margin-bottom: 8px;
  }
  .contact-list { list-style: none; font-size: 12.5px; line-height: 1.6; }
  .contact-list li { display: flex; align-items: center; gap: 8px; }
  .contact-icon { width: 10px; height: 10px; flex: none; fill: var(--accent-blue); }
  .address {
    margin-top: 12px;
    font-size: 12.5px;
    line-height: 1.45;
  }

  /* Back: brand only, silver */
  .card-back {
    display: flex;
    align-items: center;
    justify-content: center;
  }
  .card-back .brand-name {
    font-size: 44px;
    color: var(--silver);
    background: linear-gradient(180deg, #f2f2f2 0%, #a8a8a8 55%, #dcdcdc 100%);
    -webkit-background-clip: text;
    background-clip: text;
    -webkit-text-fill-color: transparent;
    margin-top: 60px;
  }
</style>
</head>
<body>
  <main class="stage">
    <section class="card card-front" aria-label="Business card front">
      <div class="brand-panel">
        <span class="brand-name">Tidal Spoon</span>
      </div>
      <div class="contact-panel">
        <p class="person-name">Marcus Hale</p>
        <p class="person-role">Managing Director</p>
        <ul class="contact-list">
          <li>
            <svg class="contact-icon" viewBox="0 0 10 10" aria-hidden="true"><path d="M2 0.5 L3.6 2.6 L2.7 3.8 Q4 6 6.2 7.3 L7.4 6.4 L9.5 8 L8.4 9.5 Q2 8.5 0.5 1.6 Z"/></svg>
            (044)987650312
          </li>
          <li>
            <svg class="contact-icon" viewBox="0 0 10 10" aria-hidden="true"><path d="M0 2 H10 V8.5 H0 Z M0.6 2.4 L5 5.6 L9.4 2.4" stroke="#0d0d0d" stroke-width="0.8"/></svg>
            hello@tidalspoon.com
          </li>
          <li>
            <svg class="contact-icon" viewBox="0 0 10 10" aria-hidden="true"><circle cx="5" cy="5" r="4.6"/></svg>
            www.tidalspoon.com
          </li>
        </ul>
        <p class="address">88, Harbour Lane Street,<br>Westport City, 40512</p>
      </div>
    </section>

    <section class="card card-back" aria-label="Business card back">
      <span class="brand-name">Tidal Spoon</span>
    </section>
  </main>
</body>
</html>
```